Black Leather Bound Gold Embossed Book Cover Art Wanted!

Need an art piece for my new book. The book will be wrapped in black leather and the art and title will be gold embossed. The art piece is to be placed in the centre of the cover. The art needs to creatively convey the messages within the book while maintaining a simple beauty and elegance to fit the overall feel of the book.

The book is not intended to make me money but is a passion project and a labour of love. I'm looking for an art piece that best expresses the ideas presented in the book.

Please check the uploaded files for a more in depth brief and a copy of the book (Don't worry, it's short!). If you gave any questions please do not hesitate to get in contact with me.
Updates

After a review of the submissions I have decided I was not overly clear in what I was after. I have updated the brief with an image that I have drawn that I would like the artists to use as a starting point and extrapolate from. Thank you everyone for their submissions so far.

Requirements
Must have
• Please see 'Book Art Brief' PDF attached
Nice to have
Should not have

```html
<!DOCTYPE html>
<html lang="en">
<head>
<meta charset="utf-8">
<title>Conversations — Cover Spread</title>
<link rel="stylesheet" href="https://fonts.googleapis.com/css2?family=Tinos:wght@400;700&display=swap">
<style>
  :root {
    --backdrop: #dcdcdc;
    --leather: #2f2f30;
    --leather-deep: #262627;
    --copper: #c8703a;
    --copper-light: #d98a4e;
    --copper-dark: #a4562a;
  }
  * { margin: 0; padding: 0; box-sizing: border-box; }
  html, body {
    width: 1200px;
    height: 1200px;
    overflow: hidden;
    background: var(--backdrop);
  }
  .spread {
    position: relative;
    width: 1200px;
    height: 1200px;
  }
  .cover {
    position: absolute;
    top: 298px;
    width: 456px;
    height: 638px;
    background: radial-gradient(ellipse at 50% 40%, var(--leather) 0%, var(--leather-deep) 100%);
    font-family: "Tinos", "Times New Roman", serif;
    color: var(--copper);
    text-align: center;
  }
  .cover--back { left: 128px; }
  .cover--front { left: 616px; }

  .flourish {
    position: absolute;
    left: 50%;
    transform: translateX(-50%);
    height: 3px;
    background: var(--copper);
    border-radius: 2px;
  }

  .title {
    position: absolute;
    left: 0;
    right: 0;
    font-weight: 400;
    line-height: 1;
    letter-spacing: 0.01em;
  }
  .subtitle {
    position: absolute;
    left: 0;
    right: 0;
    line-height: 1;
  }
  .author {
    position: absolute;
    left: 0;
    right: 0;
    line-height: 1;
    letter-spacing: 0.62em;
    padding-left: 0.62em;
  }
  .emblem {
    position: absolute;
    border-radius: 50%;
    background: radial-gradient(circle at 35% 45%, var(--copper-light) 0%, var(--copper) 55%, var(--copper-dark) 100%);
  }

  /* Front cover */
  .cover--front .flourish--top { top: 60px; width: 222px; }
  .cover--front .title { top: 88px; font-size: 42px; }
  .cover--front .subtitle { top: 131px; font-size: 16px; }
  .cover--front .flourish--bottom { top: 168px; width: 150px; }
  .cover--front .emblem { left: 94px; top: 212px; width: 268px; height: 268px; }
  .cover--front .author { top: 555px; font-size: 13px; }
  .cover--front .flourish--foot { top: 578px; width: 72px; height: 2px; }

  /* Back cover */
  .cover--back .flourish--top { top: 97px; width: 116px; height: 2px; }
  .cover--back .title { top: 110px; font-size: 21px; }
  .cover--back .subtitle { top: 132px; font-size: 8px; }
  .cover--back .flourish--bottom { top: 153px; width: 76px; height: 2px; }
  .blurb {
    position: absolute;
    top: 196px;
    left: 0;
    right: 0;
    font-size: 14px;
    line-height: 22.9px;
  }
  .cover--back .author { top: 414px; font-size: 12px; }
  .cover--back .flourish--foot { top: 436px; width: 72px; height: 2px; }
  .cover--back .emblem { left: 186px; top: 492px; width: 84px; height: 84px; }
</style>
</head>
<body>
<main class="spread">
  <section class="cover cover--back" aria-label="Back cover">
    <div class="flourish flourish--top" role="img" aria-label="Gold ornamental flourish"></div>
    <h2 class="title">CONVERSATIONS</h2>
    <p class="subtitle">headline or line from the book</p>
    <div class="flourish flourish--bottom" role="img" aria-label="Gold ornamental flourish"></div>
    <p class="blurb">
      about the book about the book about the book<br>
      about the book about the book about the book about the book<br>
      about the book about the book about the book<br>
      about the book about the book about the book<br>
      about the book about the book about the book about the book<br>
      about the book about the book<br>
      about the book about the book about the book about the book<br>
      vabout the book about the book about the book<br>
      about the book
    </p>
    <p class="author">AUTHOR NAME</p>
    <div class="flourish flourish--foot" role="img" aria-label="Gold ornamental flourish"></div>
    <div class="emblem" role="img" aria-label="Small gold embossed emblem: two interlocking stylised faces forming a yin-yang circle"></div>
  </section>

  <section class="cover cover--front" aria-label="Front cover">
    <div class="flourish flourish--top" role="img" aria-label="Gold ornamental flourish"></div>
    <h1 class="title">CONVERSATIONS</h1>
    <p class="subtitle">headline or line from the book</p>
    <div class="flourish flourish--bottom" role="img" aria-label="Gold ornamental flourish"></div>
    <div class="emblem" role="img" aria-label="Gold embossed artwork: two interlocking stylised faces in conversation forming a yin-yang circle"></div>
    <p class="author">AUTHOR NAME</p>
    <div class="flourish flourish--foot" role="img" aria-label="Gold ornamental flourish"></div>
  </section>
</main>
</body>
</html>
```